Darin Wekel Orthodontics
Business Card, Letterhead, Envelopes, Folder
@ Project holder : Please,Extend this Contest.
I am interested and Coming....
Anyone do a full size envelope where the letterhead slides in the envelope unfolded.
Anyone willing to experiment by putting the log and info at the bottom of the stationary page rather than the top.
Thanks for your submissions.#2,3,6,7 appear too busy for me. Lets stick with simplicity. Back of business card should probably have a white or light background so we can write the appoitment time in pen on the card.
ai format uploaded
kindly upload ai or eps file of logo

```html
<!DOCTYPE html>
<html lang="en">
<head>
<meta charset="utf-8">
<title>Darin Wekel Orthodontics — Letterhead</title>
<link rel="stylesheet" href="https://fonts.googleapis.com/css2?family=Open+Sans:wght@400&display=swap">
<style>
  :root {
    --backdrop: #e9e9ec;
    --paper: #ffffff;
    --band-dark: #0f3f6b;
    --band-mid: #1f5f94;
    --rule-light: #6fb3de;
    --footer-ink: #2f5f8a;
    --brand-ink: #ffffff;
  }
  * { margin: 0; padding: 0; box-sizing: border-box; }
  html, body {
    width: 1200px;
    height: 749px;
    overflow: hidden;
    background: var(--backdrop);
    font-family: "Open Sans", Arial, sans-serif;
  }
  .stage {
    width: 1200px;
    height: 749px;
    display: flex;
    align-items: center;
    justify-content: center;
  }
  .letterhead {
    position: relative;
    width: 540px;
    height: 699px;
    background: var(--paper);
    box-shadow: 0 2px 10px rgba(0, 0, 0, 0.15);
  }
  .brand-band {
    position: absolute;
    left: 0;
    right: 0;
    top: 585px;
    height: 66px;
    background: linear-gradient(90deg, var(--band-dark) 0%, var(--band-mid) 50%, var(--band-dark) 100%);
    display: flex;
    align-items: center;
    justify-content: center;
  }
  .brand-name {
    color: var(--brand-ink);
    font-size: 17px;
    font-weight: 400;
    letter-spacing: 0.5px;
  }
  .accent-rule {
    position: absolute;
    left: 0;
    right: 0;
    top: 655px;
    height: 2px;
    background: var(--rule-light);
  }
  .contact-line {
    position: absolute;
    left: 0;
    right: 0;
    top: 664px;
    text-align: center;
    font-size: 6.5px;
    color: var(--footer-ink);
    letter-spacing: 0.2px;
  }
</style>
</head>
<body>
  <main class="stage">
    <article class="letterhead">
      <div class="brand-band">
        <span class="brand-name">Darin Wekel Orthodontics</span>
      </div>
      <div class="accent-rule"></div>
      <p class="contact-line">Suite 210 | 4820 Maple Ridge Road NW | Calgary, Alberta T3A 1B2 | Phone: 403-555-0142 | www.darinwekelortho.ca</p>
    </article>
  </main>
</body>
</html>
```